LOCAL TAXI SERVICE NEEDS A BANNER AD DESIGN

NEED BANNER AD DESIGN FOR TAXI SERVICE IN NJ. WE PROVIDE LOCAL AND LONG DISTANCE TRANSPORTATION. OUR MAIN BASE OF CUSTOMER GO TO THE MAJOR AIRPORTS IN THE TRI STATE AREA. I WANT TO OFFER A SPECIAL GOING TO HOLMBRIDGE AIRPORT OF $35.00 WITH A COUPON CODE OF PW 12. THIS BANNER AD WILL BE USED FOR MY PALWIRE PAGE

Target Market(s)

PEOPLE WHO TRAVEL A LOT

Industry/Entity Type

Taxi

Font styles to use
Serif
Sans Serif

Colors
0792cd
0255a3
33a6d7
85cae6
cee9f5
ecf7fb
ffffff

Requirements
Must have
• MY COMPANY NAME: DORVAN'S TAXI

```html
<!DOCTYPE html>
<html lang="en">
<head>
<meta charset="utf-8">
<title>Dorvan's Taxi – Special Offer Banner</title>
<link href="https://fonts.googleapis.com/css2?family=Archivo+Black&family=Oswald:wght@600;700&display=swap" rel="stylesheet">
<style>
  :root {
    --sky: #0792cd;
    --royal: #0255a3;
    --azure: #33a6d7;
    --mist: #85cae6;
    --haze: #cee9f5;
    --frost: #ecf7fb;
    --white: #ffffff;
    --navy: #1b3a86;
    --silver: #c9ced6;
    --backdrop: #3a3a3c;
  }
  html, body {
    margin: 0;
    padding: 0;
    width: 1200px;
    height: 999px;
    overflow: hidden;
    background: var(--backdrop);
  }
  .banner {
    position: absolute;
    left: 47px;
    top: 217px;
    width: 1106px;
    height: 565px;
    overflow: hidden;
    background: radial-gradient(circle at 40% 45%, var(--white) 0%, var(--frost) 45%, var(--haze) 100%);
  }
  .swoosh {
    position: absolute;
    inset: 0;
  }
  .brand {
    position: absolute;
    left: 60px;
    top: 52px;
    width: 400px;
    text-align: center;
  }
  .brand-name {
    margin: 0;
    font-family: "Archivo Black", "Arial Black", sans-serif;
    font-size: 70px;
    line-height: 1;
    letter-spacing: 1px;
    color: var(--royal);
    white-space: nowrap;
  }
  .brand-badge {
    display: inline-block;
    margin-top: 14px;
    width: 263px;
    height: 110px;
    border-radius: 14px;
    background: var(--royal);
    color: var(--white);
    font-family: "Archivo Black", "Arial Black", sans-serif;
    font-size: 72px;
    line-height: 110px;
    letter-spacing: 2px;
  }
  .car-photo {
    position: absolute;
    left: 28px;
    top: 290px;
    width: 425px;
    height: 215px;
    border-radius: 60px 80px 30px 30px;
    background: linear-gradient(180deg, #f4f5f7 0%, #dfe2e6 55%, #8a8e94 100%);
  }
  .offer {
    position: absolute;
    left: 640px;
    top: 45px;
    width: 466px;
    text-align: center;
    font-family: "Oswald", "Arial Narrow", sans-serif;
    font-weight: 700;
    text-transform: uppercase;
  }
  .offer-title {
    margin: 0;
    font-size: 68px;
    line-height: 76px;
    color: var(--royal);
  }
  .offer-route {
    margin: 24px 0 0;
    font-size: 34px;
    line-height: 46px;
    color: var(--sky);
  }
  .offer-route .destination { font-size: 31px; }
  .offer-price {
    margin: 10px 0 0;
    font-size: 100px;
    line-height: 110px;
    color: var(--royal);
  }
  .offer-note {
    margin: 28px 0 0;
    font-size: 31px;
    line-height: 40px;
    color: var(--sky);
  }
  .coupon {
    display: inline-block;
    margin-top: 12px;
    width: 274px;
    height: 98px;
    border: 4px dashed var(--sky);
    border-radius: 18px;
    font-size: 88px;
    line-height: 98px;
    color: var(--royal);
  }
</style>
</head>
<body>
  <section class="banner">
    <svg class="swoosh" width="1106" height="565" viewBox="0 0 1106 565" aria-hidden="true">
      <defs>
        <linearGradient id="offer-panel" x1="0" y1="0" x2="1" y2="0">
          <stop offset="0" stop-color="#85cae6"/>
          <stop offset="0.35" stop-color="#cee9f5"/>
          <stop offset="1" stop-color="#ffffff"/>
        </linearGradient>
      </defs>
      <path d="M630 0 Q800 260 540 565 L1106 565 L1106 0 Z" fill="url(#offer-panel)"/>
      <path d="M470 0 Q640 260 380 565 L490 565 Q750 260 580 0 Z" fill="#33a6d7"/>
      <path d="M470 0 Q640 260 380 565 L430 565 Q690 260 520 0 Z" fill="#85cae6"/>
      <path d="M510 0 Q680 260 480 565 L560 565 Q780 260 590 0 Z" fill="#0255a3"/>
      <path d="M560 0 Q730 260 540 565 L575 565 Q790 260 600 0 Z" fill="#1b3a86"/>
      <path d="M600 0 Q770 260 590 565 L640 565 Q820 260 645 0 Z" fill="#c9ced6"/>
    </svg>

    <div class="brand">
      <h1 class="brand-name">DORVAN'S</h1>
      <div class="brand-badge">TAXI</div>
    </div>

    <div class="car-photo" role="img" aria-label="Photo of a white sedan taxi with a yellow roof sign"></div>

    <div class="offer">
      <h2 class="offer-title">Special Offer</h2>
      <p class="offer-route">Going to<br><span class="destination">Holmbridge Airport of</span></p>
      <p class="offer-price">$35.00</p>
      <p class="offer-note">With a coupon code of</p>
      <div class="coupon">PW 12</div>
    </div>
  </section>
</body>
</html>
```